Newsletter Ad

I am looking for someone to design an advertisement for a mother's club newsletter. 4" wide X by 5" tall (and 2.5" wide X 5" tall if possible).

I'm a psychotherapist, so want the ad to look professional, but modern. I have a logo with my photo attached that can be incorporated into the design. The colors of my website are turquoise and white. I'd like to keep with that theme...so maybe some turquoise blocking to match the logo font color.

I'm uploading a logo as well as an ad draft with the content I'd like listed in the ad.

```html
<!DOCTYPE html>
<html lang="en">
<head>
<meta charset="utf-8">
<title>Psychotherapy Newsletter Ad – Mara Ellison, MA, MFT</title>
<link rel="stylesheet" href="https://fonts.googleapis.com/css2?family=Jost:wght@400;500;600&family=Roboto+Condensed:wght@700&display=swap">
<style>
  :root {
    --teal: #23908a;
    --ink: #0b0b0b;
    --white: #ffffff;
    --paper: #ffffff;
  }
  * { margin: 0; padding: 0; box-sizing: border-box; }
  html, body { width: 982px; height: 1200px; overflow: hidden; background: var(--paper); }
  .ad { position: relative; width: 982px; height: 1200px; font-family: "Jost", "Futura", sans-serif; color: var(--white); }
  .ad-shapes { position: absolute; inset: 0; }
  .license {
    position: absolute; left: 74px; top: 80px;
    font-family: "Roboto Condensed", "Arial Narrow", sans-serif;
    font-weight: 700; font-size: 18px; letter-spacing: 0.2px;
  }
  .headline {
    position: absolute; left: 343px; top: 112px;
    font-weight: 600; font-size: 58px; line-height: 71px; letter-spacing: -0.3px;
  }
  .services {
    position: absolute; left: 476px; top: 454px;
    list-style: none; font-size: 30px; line-height: 38.6px; font-weight: 400; letter-spacing: 0.4px;
  }
  .services li { position: relative; padding-left: 24px; }
  .services li::before {
    content: ""; position: absolute; left: 2px; top: 17px;
    width: 7px; height: 7px; border-radius: 50%; background: var(--white);
  }
  .portrait {
    position: absolute; left: 55px; top: 556px; width: 305px; height: 590px;
    background: radial-gradient(ellipse at 50% 40%, #d9b49a 0%, #a98266 38%, #5e4634 70%, #1a1410 100%);
  }
  .name {
    position: absolute; left: 380px; top: 858px; white-space: nowrap;
    color: var(--teal); font-weight: 400; font-size: 44px; letter-spacing: 0;
  }
  .contact { position: absolute; left: 455px; top: 926px; list-style: none; font-size: 28px; line-height: 35px; }
  .contact li { display: flex; align-items: flex-start; }
  .contact svg { width: 22px; height: 22px; margin: 6px 20px 0 0; flex: none; fill: var(--white); }
</style>
</head>
<body>
<main class="ad">
  <svg class="ad-shapes" viewBox="0 0 982 1200" aria-hidden="true">
    <rect x="55" y="55" width="873" height="1091" fill="var(--ink)"/>
    <path d="M273 55 H928 V592 C820 470 610 378 273 387 Z" fill="var(--teal)"/>
    <path d="M273 393 C610 384 820 476 928 598" fill="none" stroke="var(--white)" stroke-width="5"/>
    <rect x="500" y="1131" width="428" height="15" fill="var(--teal)"/>
  </svg>

  <p class="license">License# MFC48215</p>

  <h1 class="headline">Psychotherapy for<br>Individuals, Couples<br>and Families</h1>

  <ul class="services">
    <li>Parenting</li>
    <li>Depression</li>
    <li>Anxiety</li>
    <li>Life Transitions</li>
    <li>Divorce</li>
    <li>Couples Issues</li>
    <li>Women’s Issues</li>
    <li>Attachment and<br>Neuroscience</li>
  </ul>

  <div class="portrait" role="img" aria-label="Portrait photo of the therapist, smiling, with long light brown hair"></div>

  <h2 class="name">MARA ELLISON, MA, MFT</h2>

  <ul class="contact">
    <li><svg viewBox="0 0 24 24"><path d="M12 1a8 8 0 0 0-8 8c0 6 8 14 8 14s8-8 8-14a8 8 0 0 0-8-8zm0 11a3 3 0 1 1 0-6 3 3 0 0 1 0 6z"/></svg><span>148 Cedar Avenue,<br>Bay Hollow, CA 94900</span></li>
    <li><svg viewBox="0 0 24 24"><path d="M12 1a11 11 0 1 0 0 22 11 11 0 0 0 0-22zm0 2c1.3 0 2.7 2.3 3.2 6H8.8C9.3 5.3 10.7 3 12 3zm-3.4.7A14 14 0 0 0 6.8 9H3.5a9 9 0 0 1 5.1-5.3zm6.8 0A9 9 0 0 1 20.5 9h-3.3a14 14 0 0 0-1.8-5.3zM3.1 11h3.6a18 18 0 0 0 0 2H3.1a9 9 0 0 1 0-2zm5.6 0h6.6a16 16 0 0 1 0 2H8.7a16 16 0 0 1 0-2zm8.6 0h3.6a9 9 0 0 1 0 2h-3.6a18 18 0 0 0 0-2zM3.5 15h3.3a14 14 0 0 0 1.8 5.3A9 9 0 0 1 3.5 15zm5.3 0h6.4c-.5 3.7-1.9 6-3.2 6s-2.7-2.3-3.2-6zm8.4 0h3.3a9 9 0 0 1-5.1 5.3 14 14 0 0 0 1.8-5.3z"/></svg><span>www.maraellison.com</span></li>
    <li><svg viewBox="0 0 24 24"><path d="M1 4h22v16H1zm2 2v.4l9 6.6 9-6.6V6zm0 2.9V18h18V8.9l-9 6.6z"/></svg><span>mara@maraellison.com</span></li>
    <li><svg viewBox="0 0 24 24"><path d="M8 1h4v6l-3 2c0 3 1 5 2 6l3-1v7h-4C6 21 4 16 4 11S5 2 8 1z"/></svg><span>415.555.0137</span></li>
  </ul>
</main>
</body>
</html>
```